METAL FABRICATION BUSINESS CARD

** I will be ending the project and picking design early. This Friday October 3rd at 7am MST if not sooner**
ONE SIDED BUSINESS CARD ONLY. AND LOGO SIZE TO BE DOMINANT so it stands out.
Looking for a black background and will be doing raised chrome/silver font on the business cards. Looking to have the following on the front of the business card. Company logo is uploaded in files.
Company logo
*Compartment Doors
*Roof Radius Metal
*J-Wrap Metal Skirting
*S-Lock Beltline Molding
*Pre-Bent Molding
and more...
Owen Baskell 406.529.1847 info@Trelvo-Works.com
Updates
One sided business card only please. Also logo size should be dominant and sized bigger
Contact Information for Business Card
Black background, Text will be raised chrome/silver, and corners will be rounded.

```html
<!DOCTYPE html>
<html lang="en">
<head>
<meta charset="UTF-8">
<title>Trelvo-Works Business Card</title>
<link rel="stylesheet" href="https://fonts.googleapis.com/css2?family=Montserrat:wght@500;700&family=Oswald:wght@500&display=swap">
<style>
  :root {
    --backdrop: #3a3a3a;
    --card-black: #111111;
    --card-edge: #1c1c1c;
    --silver: #d4d4d4;
    --silver-light: #f2f2f2;
    --silver-dark: #8c8c8c;
    --divider: #5a5a5a;
  }
  * { margin: 0; padding: 0; box-sizing: border-box; }
  html, body {
    width: 1200px; height: 1200px; overflow: hidden;
    background: var(--backdrop);
  }
  .canvas {
    position: relative; width: 1200px; height: 1200px;
    display: flex; align-items: center; justify-content: center;
  }
  .business-card {
    position: relative; width: 1050px; height: 600px;
    border-radius: 56px;
    background: linear-gradient(135deg, var(--card-edge) 0%, var(--card-black) 55%, #0a0a0a 100%);
    overflow: hidden;
    box-shadow: 0 24px 50px rgba(0,0,0,0.45);
  }
  .brand {
    position: absolute; left: 60px; top: 56px;
    display: flex; align-items: center; gap: 22px;
    white-space: nowrap;
  }
  .brand-circle {
    width: 110px; height: 110px; border-radius: 50%;
    border: 9px solid var(--silver); flex: none;
  }
  .brand-name {
    font-family: "Montserrat", sans-serif; font-weight: 700;
    font-size: 72px; letter-spacing: 0.5px; color: var(--silver);
    line-height: 1;
  }
  .contact {
    position: absolute; left: 70px; top: 300px;
    font-family: "Montserrat", sans-serif; color: var(--silver-light);
    white-space: nowrap;
  }
  .contact-name {
    font-weight: 700; font-size: 34px; letter-spacing: 5px;
    text-transform: uppercase; color: var(--silver); margin-bottom: 16px;
  }
  .contact-line {
    display: flex; align-items: center; gap: 14px;
    font-weight: 500; font-size: 30px; margin-bottom: 8px;
  }
  .contact-line svg { width: 30px; height: 30px; flex: none; }
  .divider {
    position: absolute; left: 590px; top: 230px;
    width: 2px; height: 220px; background: var(--divider);
  }
  .services {
    position: absolute; left: 635px; top: 205px; list-style: none;
    font-family: "Oswald", sans-serif; font-weight: 500;
    font-size: 30px; line-height: 44px; text-transform: uppercase;
    color: var(--silver-light); white-space: nowrap;
  }
  .services li { display: flex; align-items: center; gap: 14px; }
  .services li::before {
    content: ""; width: 11px; height: 11px; border-radius: 50%;
    background: var(--silver); flex: none;
  }
  .edge-band {
    position: absolute; left: 0; right: 0; height: 8px;
    background: linear-gradient(90deg, var(--silver-dark), var(--silver-light) 50%, var(--silver-dark));
  }
  .edge-band.upper { bottom: 62px; }
  .edge-band.lower { bottom: 40px; height: 4px; opacity: 0.7; }
</style>
</head>
<body>
<div class="canvas">
  <div class="business-card">
    <div class="brand">
      <div class="brand-circle"></div>
      <div class="brand-name">Trelvo-Works</div>
    </div>

    <div class="contact">
      <div class="contact-name">Owen Baskell</div>
      <div class="contact-line">
        <svg viewBox="0 0 24 24" aria-hidden="true"><path fill="#d4d4d4" d="M6.6 10.8a15.1 15.1 0 0 0 6.6 6.6l2.2-2.2c.3-.3.7-.4 1-.2 1.1.4 2.3.6 3.6.6.6 0 1 .4 1 1V20c0 .6-.4 1-1 1A17 17 0 0 1 3 4c0-.6.4-1 1-1h3.5c.6 0 1 .4 1 1 0 1.3.2 2.5.6 3.6.1.3 0 .7-.2 1z"/></svg>
        <span>406.529.1847</span>
      </div>
      <div class="contact-line">
        <svg viewBox="0 0 24 24" aria-hidden="true"><rect x="2" y="5" width="20" height="14" fill="none" stroke="#d4d4d4" stroke-width="2"/><path d="M2 5l10 8 10-8" fill="none" stroke="#d4d4d4" stroke-width="2"/></svg>
        <span>info@Trelvo-Works.com</span>
      </div>
    </div>

    <div class="divider"></div>

    <ul class="services">
      <li>Compartment Doors</li>
      <li>Roof Radius Metal</li>
      <li>J-Wrap Metal Skirting</li>
      <li>S-Lock Beltline Molding</li>
      <li>Pre-Bent Molding</li>
      <li>And More...</li>
    </ul>

    <div class="edge-band upper"></div>
    <div class="edge-band lower"></div>
  </div>
</div>
</body>
</html>
```